Infographic for a Life Transformation brand to showcase their principle method

I need a clean infographic which would be used in a brochure to show the 5 steps to achieving a Inner Uprising. (ie Life transformation). I use the theme of a revolution so I would like the graphic to include a raised fist or something to represent a revolution and then the 5 points of information to represent each step.
Needs to very clean and simple. I don't want something that would take up a full page, I want it as a graphic, almost like a big logo. I don't want it laid out like a process chart.

My brand personalities from https://markcharacterhub.com.au/ are
The Everyman and The Magician to give you an idea of my brand.

I've attached my logo so that you can see the colour of it. Graphic doesn't need to match logo but should align with that colour.

Target Market(s)

Top Tier Executives, males, 35-55y old

Industry/Entity Type

Life Coaching

Requirements
Must have
• The graphic must have the 5 Steps: in this order
1.Clarity
2. Measurement
3. Discipline
4. Nutrition
5.Exercise
Nice to have
• It could include these action steps which line up with the 5 steps, It may be too much information by there is the option to include if it works.
1.see it
2. track it
3. do it
4. eat it
5. move it

```html
<!DOCTYPE html>
<html lang="en">
<head>
<meta charset="utf-8">
<title>5 Steps to Achieving an Inner Uprising</title>
<link rel="stylesheet" href="https://fonts.googleapis.com/css2?family=Chakra+Petch:wght@700&family=Cinzel:wght@500&display=swap">
<style>
  :root {
    --navy: #1c3563;
    --fist-blue: #16427f;
    --step-label: #1d4587;
    --title-red: #b42a12;
    --frame-top: #f26b4f;
    --frame-bottom: #1d3c78;
    --red-900: #a81b08;
    --red-800: #c8220a;
    --red-700: #e23414;
    --red-600: #f1512f;
    --red-500: #f56d50;
    --red-400: #f88f76;
    --red-300: #fbb19f;
    --green-top: #27b760;
    --green-left: #45c46e;
    --green-right: #16a94a;
    --green-bl: #6ed88f;
    --green-br: #0a7a32;
    --white: #ffffff;
  }
  html, body {
    margin: 0;
    padding: 0;
    width: 1200px;
    height: 1000px;
    overflow: hidden;
    background: var(--white);
  }
  .canvas { display: block; width: 1200px; height: 1000px; }
  .step-label {
    font-family: "Chakra Petch", "Arial Narrow", sans-serif;
    font-weight: 700;
    font-size: 20px;
    letter-spacing: 2.5px;
    fill: var(--step-label);
  }
  .brand-name {
    font-family: "Chakra Petch", "Arial Narrow", sans-serif;
    font-weight: 700;
    font-size: 11px;
    letter-spacing: 1.2px;
    fill: var(--white);
  }
  .headline {
    font-family: "Cinzel", "Georgia", serif;
    font-weight: 500;
    font-size: 30px;
    fill: var(--title-red);
  }
  .rule { stroke: var(--title-red); stroke-width: 6; }
  .icon { fill: none; stroke: var(--white); stroke-width: 3; stroke-linecap: round; stroke-linejoin: round; }
</style>
</head>
<body>
<svg class="canvas" viewBox="0 0 1200 1000" xmlns="http://www.w3.org/2000/svg">
  <defs>
    <linearGradient id="frame-gradient" x1="0" y1="0" x2="0" y2="1">
      <stop offset="0" stop-color="var(--frame-top)"/>
      <stop offset="0.45" stop-color="#c8331c"/>
      <stop offset="0.6" stop-color="var(--frame-bottom)"/>
      <stop offset="1" stop-color="var(--navy)"/>
    </linearGradient>
    <polygon id="pentagon" points="0,-285 -259,-92 -165,215 165,215 261,-92"/>
  </defs>

  <!-- Layered pentagon -->
  <g class="pentagon-stack" transform="translate(577 470)">
    <use href="#pentagon" transform="scale(1.08)" fill="none" stroke="url(#frame-gradient)" stroke-width="5"/>
    <use href="#pentagon" transform="scale(1.03)" fill="var(--red-900)"/>
    <use href="#pentagon" transform="scale(0.92)" fill="var(--red-800)"/>
    <use href="#pentagon" transform="scale(0.80)" fill="var(--red-700)"/>
    <use href="#pentagon" transform="scale(0.68)" fill="var(--red-600)"/>
    <use href="#pentagon" transform="scale(0.56)" fill="var(--red-500)"/>
    <use href="#pentagon" transform="scale(0.44)" fill="var(--red-400)"/>
    <use href="#pentagon" transform="scale(0.32)" fill="var(--red-300)"/>
  </g>

  <!-- Step labels along the edges -->
  <text class="step-label" transform="translate(428 262) rotate(-36)" text-anchor="middle">2. MEASUREMENT</text>
  <text class="step-label" transform="translate(726 262) rotate(36)" text-anchor="middle">3. DISCIPLINE</text>
  <text class="step-label" transform="translate(326 540) rotate(72)" text-anchor="middle">1.CLARITY</text>
  <text class="step-label" transform="translate(830 540) rotate(-72)" text-anchor="middle">4. NUTRITION</text>
  <text class="step-label" x="577" y="725" text-anchor="middle">5. EXERCISE</text>

  <!-- Raised fist emblem area -->
  <g class="fist-emblem">
    <path role="img" aria-label="Illustration of a raised fist, symbol of revolution"
          fill="var(--fist-blue)" stroke="var(--white)" stroke-width="6" stroke-linejoin="round"
          d="M472 312 H646 Q680 312 680 346 V468 Q680 518 650 522 L660 685 H503 L510 522 Q436 518 436 468 V346 Q436 312 472 312 Z"/>
    <text class="brand-name" x="583" y="655" text-anchor="middle">INNER UPRISING</text>
  </g>

  <!-- Step nodes -->
  <g class="node node-measurement">
    <circle cx="577" cy="185" r="57" fill="var(--frame-top)"/>
    <circle cx="577" cy="185" r="50" fill="var(--white)"/>
    <circle cx="577" cy="185" r="45" fill="var(--green-top)" stroke="var(--navy)" stroke-width="2"/>
    <g class="icon">
      <line x1="559" y1="166" x2="559" y2="204"/><circle cx="559" cy="192" r="5" fill="var(--green-top)"/>
      <line x1="577" y1="166" x2="577" y2="204"/><circle cx="577" cy="178" r="5" fill="var(--green-top)"/>
      <line x1="595" y1="166" x2="595" y2="204"/><circle cx="595" cy="186" r="5" fill="var(--green-top)"/>
    </g>
  </g>

  <g class="node node-clarity">
    <circle cx="318" cy="378" r="57" fill="#8a3148"/>
    <circle cx="318" cy="378" r="50" fill="var(--white)"/>
    <circle cx="318" cy="378" r="45" fill="var(--green-left)" stroke="var(--navy)" stroke-width="2"/>
    <g class="icon">
      <line x1="294" y1="370" x2="294" y2="386"/><line x1="342" y1="370" x2="342" y2="386"/>
      <line x1="300" y1="378" x2="336" y2="378"/>
      <polyline points="305,373 300,378 305,383"/><polyline points="331,373 336,378 331,383"/>
    </g>
  </g>

  <g class="node node-nutrition">
    <circle cx="838" cy="378" r="57" fill="#5a2c55"/>
    <circle cx="838" cy="378" r="50" fill="var(--white)"/>
    <circle cx="838" cy="378" r="45" fill="var(--green-right)" stroke="var(--navy)" stroke-width="2"/>
    <g class="icon">
      <circle cx="838" cy="378" r="24"/>
      <line x1="838" y1="356" x2="838" y2="400"/>
      <line x1="818" y1="367" x2="858" y2="389"/>
      <line x1="818" y1="389" x2="858" y2="367"/>
    </g>
  </g>

  <g class="node node-vision">
    <circle cx="412" cy="685" r="57" fill="var(--navy)"/>
    <circle cx="412" cy="685" r="50" fill="var(--white)"/>
    <circle cx="412" cy="685" r="45" fill="var(--green-bl)" stroke="var(--navy)" stroke-width="2"/>
    <g class="icon">
      <path d="M384 685 Q412 660 440 685 Q412 710 384 685 Z"/>
      <circle cx="412" cy="685" r="9"/>
      <circle cx="408" cy="681" r="2.5" fill="var(--white)"/>
    </g>
  </g>

  <g class="node node-exercise">
    <circle cx="742" cy="685" r="57" fill="var(--navy)"/>
    <circle cx="742" cy="685" r="50" fill="var(--white)"/>
    <circle cx="742" cy="685" r="45" fill="var(--green-br)" stroke="var(--navy)" stroke-width="2"/>
    <g class="icon">
      <line x1="716" y1="684" x2="768" y2="684"/>
      <line x1="720" y1="677" x2="720" y2="691"/><line x1="725" y1="679" x2="725" y2="689"/>
      <line x1="764" y1="677" x2="764" y2="691"/><line x1="759" y1="679" x2="759" y2="689"/>
      <path d="M742 700 L731 687 Q726 678 733 673 Q739 670 742 676 Q745 670 751 673 Q758 678 753 687 Z"/>
    </g>
  </g>

  <!-- Headline -->
  <g class="headline-block">
    <line class="rule" x1="313" y1="829" x2="357" y2="829"/>
    <line class="rule" x1="795" y1="829" x2="839" y2="829"/>
    <text class="headline" x="395" y="816" textLength="355" lengthAdjust="spacingAndGlyphs">5 STEPS TO ACHIEVING</text>
    <text class="headline" x="380" y="862" textLength="398" lengthAdjust="spacingAndGlyphs">an Inner Uprising</text>
  </g>
</svg>
</body>
</html>
```